Medical Cannabis company is looking for a LOGO design *

SILVER MERIDIAN (SM) is a new company in the Israeli medical cannabis industry. We will engage in PREMIUM medical cannabis growing and cultivation and also manufacturing of HIGH-END cannabis based medical products.
the design should reflect luxury, high-end and Pharma-grade products.
the design should use color GOLD and NOT using the famous cannabis leaf !

Target Market(s)

international medical cannabis Pharmaceutical companies
and of course local and international patients

Contact Information for Business Card

Ron Ben-Amit
Founder and CEO

Silver Meridian
Medical grade cannabis

ronbenamit@mailpost-example.com
972-52-3186407

Colors
ffc214
fbed22

Requirements
Must have
• clean and simple
• luxury
• gold !!
• (can also have green for Cannabis and/or blue for Pharma)
Should not have
• cannabis leaf

```html
<!DOCTYPE html>
<html lang="en">
<head>
<meta charset="utf-8">
<title>Silver Meridian — Business Card</title>
<link rel="stylesheet" href="https://fonts.googleapis.com/css2?family=Open+Sans:wght@400;600;700&display=swap">
<style>
  :root {
    --page-bg: #d6d6d6;
    --card-white: #f7f8f7;
    --card-dark: #2b2b2b;
    --card-dark-glow: #3c3e3c;
    --brand-green: #1fae3c;
    --brand-gold: #ffc214;
    --ink: #1c1c1c;
    --ink-soft: #555555;
  }
  * { box-sizing: border-box; margin: 0; padding: 0; }
  html, body { width: 1200px; height: 800px; overflow: hidden; }
  body {
    background: var(--page-bg);
    display: flex;
    align-items: center;
    justify-content: center;
    gap: 48px;
    font-family: "Open Sans", Arial, sans-serif;
  }
  .card {
    position: relative;
    width: 525px;
    height: 300px;
    overflow: hidden;
    box-shadow: 0 6px 18px rgba(0,0,0,0.18);
  }

  /* Front */
  .card-front { background: var(--card-white); color: var(--ink); }
  .brand {
    position: absolute;
    right: 58px;
    top: 54px;
    text-align: right;
  }
  .brand-name {
    font-weight: 400;
    font-size: 26px;
    color: var(--ink);
    line-height: 1.1;
  }
  .brand-tagline {
    margin-top: 6px;
    font-size: 9px;
    font-weight: 600;
    letter-spacing: 3px;
    color: var(--brand-green);
  }
  .person {
    position: absolute;
    left: 40px;
    top: 148px;
  }
  .person-name {
    font-weight: 700;
    font-size: 13px;
    letter-spacing: 4px;
  }
  .person-title {
    font-size: 9px;
    letter-spacing: 3px;
    color: var(--ink-soft);
    margin-top: 2px;
  }
  .contact-list {
    position: absolute;
    left: 40px;
    top: 196px;
    list-style: none;
  }
  .contact-item {
    display: flex;
    align-items: center;
    gap: 10px;
    font-size: 9.5px;
    letter-spacing: 2.6px;
    font-weight: 600;
    line-height: 19px;
    white-space: nowrap;
  }
  .contact-icon { width: 11px; height: 11px; fill: var(--ink); flex: none; }

  /* Back */
  .card-back {
    background: radial-gradient(ellipse 70% 60% at 45% 35%, var(--card-dark-glow), var(--card-dark) 75%);
  }
  .gold-band {
    position: absolute;
    left: 58%;
    right: 0;
    top: 176px;
    height: 40px;
    background: var(--brand-gold);
  }
  .back-brand {
    position: absolute;
    right: 42%;
    margin-right: 8px;
    top: 178px;
    text-align: right;
    direction: rtl;
    color: var(--brand-gold);
  }
  .back-brand-name { font-size: 24px; font-weight: 400; line-height: 1.1; }
  .back-brand-tagline { font-size: 11px; font-weight: 400; letter-spacing: 2px; margin-top: 4px; }
</style>
</head>
<body>

  <section class="card card-front">
    <div class="brand">
      <div class="brand-name">Silver Meridian</div>
      <div class="brand-tagline">MEDICAL GRADE CANNABIS</div>
    </div>

    <div class="person">
      <div class="person-name">RON BEN-AMIT</div>
      <div class="person-title">FOUNDER AND CEO</div>
    </div>

    <ul class="contact-list">
      <li class="contact-item">
        <svg class="contact-icon" viewBox="0 0 12 12"><path d="M0 2h12v8H0z" fill="none" stroke="#1c1c1c" stroke-width="1.4"/><path d="M0 2l6 4.5L12 2" fill="none" stroke="#1c1c1c" stroke-width="1.4"/></svg>
        RONBENAMIT@MAILPOST-EXAMPLE.COM
      </li>
      <li class="contact-item">
        <svg class="contact-icon" viewBox="0 0 12 12"><circle cx="6" cy="6" r="5" fill="none" stroke="#1c1c1c" stroke-width="1.3"/><ellipse cx="6" cy="6" rx="2.2" ry="5" fill="none" stroke="#1c1c1c" stroke-width="1.1"/><path d="M1 6h10" stroke="#1c1c1c" stroke-width="1.1"/></svg>
        WWW.SILVERMERIDIAN-EXAMPLE.COM
      </li>
      <li class="contact-item">
        <svg class="contact-icon" viewBox="0 0 12 12"><path d="M2.5 1l2 2.5-1.2 1.3c.7 1.5 1.9 2.7 3.4 3.4L8 7l2.5 2-1 2C5 11 1 7 1 2.5z"/></svg>
        972-52-3186407
      </li>
      <li class="contact-item">
        <svg class="contact-icon" viewBox="0 0 12 12"><path d="M6 0.5a4 4 0 0 0-4 4c0 3 4 7 4 7s4-4 4-7a4 4 0 0 0-4-4zm0 5.7a1.7 1.7 0 1 1 0-3.4 1.7 1.7 0 0 1 0 3.4z"/></svg>
        8 OLIVE GROVE STREET MODIIN CENTER | ISRAEL
      </li>
    </ul>
  </section>

  <section class="card card-back">
    <div class="gold-band"></div>
    <div class="back-brand">
      <div class="back-brand-name">סילבר מרידיאן</div>
      <div class="back-brand-tagline">קנאביס רפואי</div>
    </div>
  </section>

</body>
</html>
```